**** Business card design for VoltaNode ****

For my ICT company VoltaNode I need I need a business card design.

We design, build and host web-applications and we have our own CMS product.

Some good examples are attached.

The information should be:
Joris Tielenburg
Managing director
E: j.tielenburg@voltanode-example.nl
M: +31(0)6 57218064
T: +31(0)40 7249305
W: www.voltanode-example.nl

Address:
Berend Vlootweg 27
5612 KT Eindhoven

Industry/Entity Type

Business

Requirements
Must have
• - Use logo (see attachments)
- Double sided
- Distinctive
Nice to have
• - Place for a statement on the back-side: "Designed with knowledge, built with passion"
- HTML code (or Wordpress)
- Dark (black or dark-gray) side
- Small simple images for telephone, e-mail en Url.
- QR code (only if not disturbing), not required, just an option

```html
<!DOCTYPE html>
<html lang="en">
<head>
<meta charset="utf-8">
<title>VoltaNode business card – statement side</title>
<link rel="stylesheet" href="https://fonts.googleapis.com/css2?family=Open+Sans:wght@400&display=swap">
<style>
  :root {
    --card-black: #000000;
    --brand-blue: #29a8e0;
    --frame-blue: #3aa9dd;
  }
  html, body {
    margin: 0;
    padding: 0;
    width: 1200px;
    height: 736px;
    overflow: hidden;
    background: var(--card-black);
  }
  .card-back {
    position: relative;
    width: 1200px;
    height: 736px;
    box-sizing: border-box;
    border: 5px solid var(--frame-blue);
    background: var(--card-black);
    font-family: "Open Sans", "Myriad Pro", Arial, sans-serif;
    color: var(--brand-blue);
  }
  .statement-line {
    position: absolute;
    margin: 0;
    font-size: 53px;
    font-weight: 400;
    line-height: 1;
    letter-spacing: -0.8px;
    white-space: nowrap;
  }
  .statement-design { left: 173px; top: 277px; }
  .statement-build { left: 497px; top: 344px; }
</style>
</head>
<body>
  <main class="card-back">
    <p class="statement-line statement-design">Designed with knowledge...</p>
    <p class="statement-line statement-build">Built with passion...</p>
  </main>
</body>
</html>
```